Package Design for Plant-based Dumplings

We need a CPG Package design for a new product we're launching. I included example (front and back) of what a typical information food package has, so you can use it as reference.

Target Market(s)

Consumers that are seeking non-meat items. Environment concerned consumers.

Colors

Designer to choose colors to be used in the design.

Requirements
Must have
• Modern and clean looking design.
Nice to have
• might have multiple flavors, so make design where it could be have multiple variations.

```html
<!DOCTYPE html>
<html lang="en">
<head>
<meta charset="utf-8">
<title>MiraSong Foods – Plant-Based Dumplings Package</title>
<link href="https://fonts.googleapis.com/css2?family=Kalam:wght@400;700&family=Mulish:wght@400;600&family=Arimo:wght@400;700&display=swap" rel="stylesheet">
<style>
:root{
  --ink:#141210;
  --panel:#1a1816;
  --orange:#f7921e;
  --white:#ffffff;
  --paper:#ffffff;
  --rule:#000000;
}
*{margin:0;padding:0;box-sizing:border-box}
html,body{width:1200px;height:921px;overflow:hidden;background:var(--white)}
.sheet{position:relative;width:1200px;height:921px}
.panel{position:absolute;top:0;width:583px;height:921px;background:var(--panel);overflow:hidden;color:var(--white)}
.panel--front{left:0}
.panel--back{left:617px}
.abs{position:absolute}
.band{position:absolute;left:0;top:0}
.photo{position:absolute}
.photo--front{left:104px;top:472px;width:373px;height:384px;border-radius:50%;
  background:radial-gradient(circle at 50% 50%,#d9c7a0 0%,#b89a68 28%,#5a4a35 48%,#2a2623 62%,#1f1d1b 100%)}
.photo--back{left:0;top:0;width:330px;height:380px;border-radius:0 0 60% 0;
  background:radial-gradient(circle at 35% 35%,#d8c8a4 0%,#a88d62 35%,#3e3830 65%,#1a1816 100%)}
.brand-name{position:absolute;font-family:'Kalam',cursive;font-weight:700;font-size:30px;line-height:1;color:var(--ink);white-space:nowrap}
.script{font-family:'Kalam',cursive;color:var(--orange);white-space:nowrap}
.kicker{font-weight:400;letter-spacing:4px;font-style:italic}
.title{font-weight:700;letter-spacing:2px;font-style:italic;line-height:1}
.tagline{font-family:'Kalam',cursive;color:var(--white);font-style:italic;white-space:nowrap}
.badges{position:absolute;left:485px;top:556px;width:66px;text-align:center;font-family:'Arimo',sans-serif;font-weight:700;font-size:9.5px;line-height:1.25}
.badges hr{border:0;border-top:1.5px solid var(--white);margin:6px 0}
.badges svg{display:block;margin:4px auto 0}
.badge-vegan{font-family:'Kalam',cursive;font-size:22px;font-style:italic;font-weight:700}
.protein{left:49px;top:780px;font-family:'Arimo',sans-serif;font-weight:700;line-height:1}
.protein__num{font-size:38px;color:var(--orange)}
.protein__of{font-size:15px}
.protein__label{display:block;font-size:15px;margin-top:2px}
.footline{font-family:'Kalam',cursive;font-size:24px;top:852px;white-space:nowrap}
.instructions{left:36px;top:388px;width:512px;height:150px;border:1.5px solid var(--white);border-radius:6px;padding:3px 4px;
  font-family:'Mulish',sans-serif;font-size:10.2px;line-height:13.9px}
.instructions__head{border-bottom:1.5px solid var(--white);width:96%}
.instructions ol{list-style:none;padding-left:23px}
.nutrition{left:36px;top:551px;width:188px;height:337px;background:var(--paper);color:#000;padding:3px 6px;font-family:'Arimo',sans-serif;font-size:8px;line-height:1.1;overflow:hidden}
.nutrition__title{font-weight:700;font-size:21px;line-height:1.05;border-bottom:1px solid var(--rule)}
.nutrition__row{display:flex;justify-content:space-between;border-top:1px solid #999;padding:1.5px 0 1px}
.nutrition__row--indent{padding-left:9px}
.nutrition__row--indent2{padding-left:20px}
.nutrition__bar-thick{height:6px;background:var(--rule);margin:2px 0}
.nutrition__bar-mid{height:3px;background:var(--rule);margin:2px 0}
.nutrition__note{font-size:5.8px;line-height:1.25}
.b{font-weight:700}
.story{left:243px;top:551px;width:305px;font-family:'Mulish',sans-serif;font-size:10.2px;line-height:13.2px;text-align:justify}
.maker{left:221px;top:853px;width:200px;text-align:center;font-family:'Arimo',sans-serif;font-size:10.5px;letter-spacing:1.3px;line-height:13px;white-space:nowrap}
.label-blank{left:415px;top:814px;width:133px;height:77px;background:var(--paper)}
</style>
</head>
<body>
<div class="sheet">

  <section class="panel panel--front">
    <svg class="band" width="583" height="290" viewBox="0 0 583 290" aria-hidden="true">
      <path d="M0 105 L140 45 L320 18 L583 0 L583 168 L470 222 L330 238 L180 262 L60 275 L0 250 Z" fill="var(--orange)"/>
    </svg>
    <div class="brand-name" style="left:189px;top:188px">MiraSong Foods</div>
    <div class="abs script kicker" style="left:183px;top:310px;font-size:27px">PLANT-BASED</div>
    <div class="abs script title" style="left:82px;top:342px;font-size:76px">DUMPLINGS</div>
    <div class="abs tagline" style="left:95px;top:413px;font-size:23px">Using Plant-based Meat and Vegetables</div>

    <div class="photo photo--front" role="img" aria-label="Pan-fried dumplings with sesame seeds in a cast iron skillet"></div>

    <div class="badges">
      NO SOY
      <svg width="40" height="40" viewBox="0 0 40 40" aria-hidden="true">
        <ellipse cx="22" cy="18" rx="8" ry="13" transform="rotate(35 22 18)" fill="var(--white)"/>
        <line x1="4" y1="4" x2="36" y2="36" stroke="var(--white)" stroke-width="3"/>
      </svg>
      <hr>
      READY IN<br>MINUTES
      <svg width="44" height="40" viewBox="0 0 44 40" aria-hidden="true" fill="none" stroke="var(--white)" stroke-width="1.5">
        <path d="M14 2 l3 4 -3 4 M22 2 l3 4 -3 4 M30 2 l3 4 -3 4"/>
        <path d="M4 16 H40 L36 26 H8 Z" fill="var(--white)"/>
        <path d="M12 32 h20 M14 36 h16"/>
      </svg>
      <hr>
      <div class="badge-vegan">Vegan</div>
    </div>

    <div class="abs protein">
      <span class="protein__num">20g</span> <span class="protein__of">of</span>
      <span class="protein__label">Protein</span>
    </div>
    <div class="abs footline" style="left:48px">Keep Frozen</div>
    <div class="abs footline" style="left:329px">Net Wt. 2 LBs (32oz)</div>
  </section>

  <section class="panel panel--back">
    <div class="photo photo--back" role="img" aria-label="Close-up of golden pan-fried dumplings in a skillet"></div>
    <svg class="band" width="583" height="290" viewBox="0 0 583 290" aria-hidden="true">
      <path d="M20 150 L180 110 L380 70 L583 50 L583 175 L450 215 L300 240 L150 262 L30 270 Z" fill="var(--orange)"/>
    </svg>
    <div class="brand-name" style="left:187px;top:188px">MiraSong Foods</div>
    <div class="abs script kicker" style="left:238px;top:268px;font-size:23px">PLANT-BASED</div>
    <div class="abs script title" style="left:164px;top:291px;font-size:59px">DUMPLINGS</div>
    <div class="abs tagline" style="left:175px;top:349px;font-size:17px">Using Plant-based Meat and Vegetables</div>

    <div class="abs instructions">
      <div class="instructions__head">Heating Instructions</div>
      <div>Steam:</div>
      <ol><li>1. Remove frozen dumplings from the package and place them in a steamer over boiling water.</li>
      <li>2. Cover the steamer approximately 8-10 minutes or until cooked thoroughly.</li></ol>
      <div>Pan Fry:</div>
      <ol><li>1. Heat 2 teaspoons of oil in frying pan. Carefully place thawed dumplings into heated pan.</li>
      <li>2. Heat approximately 3-4 minutes or until golden brown.</li></ol>
      <div>Microwave:</div>
      <ol><li>1. Place frozen dumplings on microwave-safe dish.</li>
      <li>2. Cover with damp paper towel and heat on high for 2 to 3 minutes or until hot.</li></ol>
    </div>

    <div class="abs nutrition">
      <div class="nutrition__title">Nutrition Facts</div>
      <div style="font-size:9.5px">about 8 servings per container</div>
      <div style="display:flex;justify-content:space-between;font-size:9.5px" class="b"><span>Servings Size</span><span>3 pieces (90g)</span></div>
      <div class="nutrition__bar-thick"></div>
      <div class="b" style="font-size:7px">Amount per serving</div>
      <div style="display:flex;justify-content:space-between;align-items:flex-end;font-weight:700;line-height:1"><span style="font-size:17px">Calories</span><span style="font-size:23px">180</span></div>
      <div class="nutrition__bar-mid"></div>
      <div style="text-align:right;font-size:7px" class="b">% Daily Value</div>
      <div class="nutrition__row"><span><span class="b">Total Fat</span> 8g</span><span class="b">10%</span></div>
      <div class="nutrition__row nutrition__row--indent"><span>Saturdated Fat 2.5g</span><span class="b">13%</span></div>
      <div class="nutrition__row nutrition__row--indent"><span><i>Trans</i> Fat 0g</span><span></span></div>
      <div class="nutrition__row"><span><span class="b">Cholesterol</span> 15mg</span><span class="b">5%</span></div>
      <div class="nutrition__row"><span><span class="b">Sodium</span> 410mg</span><span class="b">18%</span></div>
      <div class="nutrition__row"><span><span class="b">Total Carbohydrate</span> 19g</span><span class="b">7%</span></div>
      <div class="nutrition__row nutrition__row--indent"><span>Dietary Fiber 1g</span><span class="b">4%</span></div>
      <div class="nutrition__row nutrition__row--indent"><span>Total Sugars 2g</span><span></span></div>
      <div class="nutrition__row nutrition__row--indent2"><span>Includes 1g Added Sugars</span><span class="b">2%</span></div>
      <div class="nutrition__row"><span><span class="b">Protein</span> 8g</span><span></span></div>
      <div class="nutrition__bar-thick"></div>
      <div class="nutrition__row" style="border-top:0"><span>Vitamin D 0mcg</span><span>0%</span></div>
      <div class="nutrition__row"><span>Calcium 30mg</span><span>2%</span></div>
      <div class="nutrition__row"><span>Iron 1.2mg</span><span>6%</span></div>
      <div class="nutrition__row"><span>Potassium 176mg</span><span>4%</span></div>
      <div class="nutrition__bar-mid"></div>
      <div class="nutrition__note">* The % Daily Value tells you how much a nutrient in a serving of food contributes to a daily diet. 2000 calories a day is used for general nutrition advise.</div>
    </div>

    <div class="abs story">
      <p>Story of the Brand somewhere on the back</p>
      <p>&emsp;The brand name MiraSong Foods was inspired from a lady named Mira Song that started a food business in S. Korea during the 1950s. Mira's family immigrated to the U.S. in late 1990s and the Song family began making dumplings out-of-their home kitchen and sold into local markets. Business grew and the family eventually built a state-of-the-art USDA food factory in 2003. Dumplings made at MiraSong's factory is now available throughout retailers in US and Canada.</p>
      <p style="margin-top:4px">&bull;&ensp;Ingredient List</p>
      <p>FILLING: Plant-Based Meat (Water, Pea Protein Isolate, Canola and Sunflower Oil, Rice Flour, Spice, Tomato Powder, Contains 0.5% or less: Yeast Extract, Sugar, Potassium Chloride, Tapioca Maltodextrin, Citric Acid, Salt, Acacia Gum, Onion Extract, Natural Flavor, Garlic Extract ), Cabbage, Onion, Sweet Potato Noodle (water, Sweet potato starch), Green Onion, Seasoning (Onion Powder, Grilled Flavor, Sugar, Garlic Dehydrated, Spice, Natural Flavor, Yeast Extract), carrot, Water, starch (cornstarch, modified starch), sesame</p>
    </div>

    <div class="abs maker">MANUFACTURED FOR:<br>NORTHFIELD COMPANY<br>SPRINGDALE, CA 90000</div>
    <div class="abs label-blank"></div>
  </section>

</div>
</body>
</html>
```